Web Design for online C2C site

We need a web design for a brand new website that has users logging into an account and uploading pictures of goods and services that they want to trade.
We like 'fresh' and simple websites that have a white background, with easy navigation, a splash of colour (grey, blue, and green is a colour scheme that appeals to us) but doesn't look overly boring.
The site needs a modern look for an old type of trade - a barter system.
We have attached a file with our logo and would like to use the top logo from the file (grey, green, and blue)
Updates
Project Deadline Extended
Reason: The timeline has been extended until this Sunday, December 2nd for all who require extra time to design a web layout.
Cheers,
Marisol
Industry/Entity Type
Trade
Look and feel
Each slider illustrates characteristics of the customer's brand and the style your logo design should communicate.

```html
<!DOCTYPE html>
<html lang="en">
<head>
<meta charset="utf-8">
<title>BarterNest – Home</title>
<link rel="stylesheet" href="https://fonts.googleapis.com/css2?family=Ubuntu:ital,wght@0,400;0,500;0,700;1,400&display=swap">
<style>
:root{
  --blue:#0a96e8;
  --blue-dark:#2a63d6;
  --blue-light:#78cdf8;
  --blue-pale:#bfe6fb;
  --green:#58c21e;
  --grey:#5b5b5b;
  --grey-light:#f4f4f4;
  --ink:#333;
  --white:#fff;
  --line:#e4e4e4;
}
*{box-sizing:border-box;margin:0;padding:0}
html,body{width:1152px;height:1200px;overflow:hidden;background:var(--white);font-family:"Ubuntu",sans-serif;color:var(--ink)}
.canvas{position:relative;width:1152px;height:1200px}
.abs{position:absolute}

/* header */
.header{left:0;top:0;width:1152px;height:174px;background:linear-gradient(#fafafa,#ececec);border-top:8px solid var(--blue)}
.brand{left:36px;top:52px;display:flex;align-items:center;gap:12px}
.brand-dot{width:62px;height:62px;border-radius:50%;background:var(--grey)}
.brand-name{font-size:40px;font-weight:500;color:var(--blue-dark);letter-spacing:-.5px}
.social{left:414px;top:0;width:228px;height:50px;background:var(--blue);border-radius:0 0 22px 22px;border:2px solid #d8eefb;border-top:0;display:flex;gap:6px;justify-content:center;align-items:center}
.social span{width:32px;height:32px;border-radius:50%;background:linear-gradient(#fff,#cfd6dc);border:1px solid #9fb3c4}
.tooltip{left:512px;top:54px;background:var(--blue-dark);color:var(--white);font-size:11px;padding:2px 8px}
.login{left:684px;top:0;width:438px;height:50px;background:var(--blue);border-radius:0 0 22px 22px;border:2px solid #d8eefb;border-top:0;display:flex;align-items:center;gap:8px;padding-left:12px}
.login label{color:var(--white);font-weight:500;font-size:18px}
.login .field{width:154px;height:32px;border-radius:16px;background:var(--white);font-size:18px;color:#777;padding:5px 14px}
.login .go{width:32px;height:32px}

/* nav */
.nav{left:0;top:174px;width:1152px;height:76px;background:var(--blue);border-top:14px solid var(--blue-dark);box-shadow:0 6px 8px -6px #bbb}
.nav-tab{left:44px;top:176px;width:148px;height:63px;background:linear-gradient(#fff,#eef0f2);border-radius:4px 4px 2px 2px;color:var(--blue-dark);font-size:23px;display:flex;align-items:center;justify-content:center}
.nav-link{top:194px;color:var(--white);font-size:23px}
.search{left:898px;top:198px;width:236px;height:35px;border-radius:18px;background:var(--white);border:1px solid #9cc;font-style:italic;font-size:17px;color:var(--blue-dark);padding:6px 16px}
.search svg{position:absolute;right:-2px;top:-2px}

/* slider */
.slider{left:96px;top:305px;width:960px;height:391px;background:#f7f7f7;box-shadow:0 10px 10px -8px #aaa}
.slide-brand{left:240px;top:120px;display:flex;align-items:center;gap:24px}
.slide-brand .brand-dot{width:150px;height:150px}
.slide-brand .brand-name{font-size:78px}
.arrow{top:463px;width:41px;height:45px;background:#333;border:2px solid #9fd2ea}
.dots{left:512px;top:667px;display:flex;gap:18px;align-items:center}
.dots span{width:16px;height:16px;border-radius:50%;background:radial-gradient(#fff,#ccc);border:1px solid #aaa}
.dots .on{width:22px;height:22px;background:radial-gradient(#2a63d6,#7bb6f4);border-color:#7bb6f4}

/* listings */
.listings{left:37px;top:788px;width:631px;height:382px;background:#fafafa;border:1px solid var(--line)}
.tab{top:0;height:41px;font-size:21px;padding:6px 20px;background:var(--blue-pale);color:#1e5fa3;border-bottom:6px solid var(--blue-light)}
.tab.active{background:#fafafa;color:var(--ink);border-bottom:0}
.divider{left:275px;top:75px;width:1px;height:306px;background:#9fd2ea}
.thumb{border-radius:4px}
.blurb{font-size:16px;line-height:21.6px;color:#333}
.play{width:30px;height:30px}

/* join panel */
.join{left:742px;top:742px;width:364px;height:424px;background:var(--white);border:1px solid #ccc;border-radius:6px;overflow:hidden;box-shadow:0 2px 4px #ccc}
.join-tab{top:0;height:46px;width:172px;font-size:20px;font-weight:500;display:flex;align-items:center;justify-content:center}
.join-tab.active{left:0;color:#1e5fa3;background:var(--white)}
.join-tab.other{left:172px;color:var(--white);background:var(--blue);border-radius:6px 6px 0 0;font-weight:400}
.join-bar{left:0;top:46px;width:364px;height:18px;background:var(--blue)}
.join-field{left:62px;width:266px;height:37px;border-radius:18px;background:var(--blue-light);border:1px solid #5fb8e8;font-size:18px;color:#1e5fa3;padding:7px 24px}
.signup{left:212px;top:315px;width:115px;height:37px;border-radius:6px;background:linear-gradient(#a8e0fc,#64c2f4);border:1px solid #58a8d8;color:#1e5fa3;font-size:19px;text-align:center;padding-top:7px}
.forgot{left:28px;top:380px;font-size:16px;color:#1e6fa8}
.join-foot{left:0;top:402px;width:364px;height:22px;background:var(--blue)}
</style>
</head>
<body>
<div class="canvas">

  <header class="abs header"></header>
  <div class="abs brand"><span class="brand-dot"></span><span class="brand-name">BarterNest</span></div>

  <div class="abs social" aria-label="Social links">
    <span></span><span></span><span></span><span></span><span></span>
  </div>
  <div class="abs tooltip">Follow us on Chirper</div>

  <form class="abs login">
    <label>Log in</label>
    <span class="field">Email</span>
    <span class="field">Password</span>
    <svg class="go" viewBox="0 0 32 32"><circle cx="16" cy="16" r="13" fill="none" stroke="#fff" stroke-width="3"/><path d="M9 16h13M17 10l6 6-6 6" fill="none" stroke="#fff" stroke-width="3"/></svg>
  </form>

  <nav class="abs nav"></nav>
  <div class="abs nav-tab">Home</div>
  <span class="abs nav-link" style="left:230px">Page</span>
  <span class="abs nav-link" style="left:334px">About us</span>
  <span class="abs nav-link" style="left:467px">Contact us</span>
  <div class="abs search">Search.....
    <svg width="37" height="37" viewBox="0 0 37 37"><circle cx="18.5" cy="18.5" r="17" fill="#233"/><circle cx="17" cy="17" r="7" fill="none" stroke="#fff" stroke-width="2.5"/><path d="M22 22l6 6" stroke="#fff" stroke-width="3"/></svg>
  </div>

  <section class="abs slider">
    <div class="abs slide-brand"><span class="brand-dot"></span><span class="brand-name">BarterNest</span></div>
  </section>
  <div class="abs arrow" style="left:44px"><svg width="37" height="41" viewBox="0 0 37 41"><path d="M24 8L11 20.5 24 33" fill="none" stroke="#eee" stroke-width="3"/></svg></div>
  <div class="abs arrow" style="left:1069px"><svg width="37" height="41" viewBox="0 0 37 41"><path d="M13 8l13 12.5L13 33" fill="none" stroke="#eee" stroke-width="3"/></svg></div>
  <div class="abs dots"><span></span><span class="on"></span><span></span><span></span></div>

  <section class="abs listings">
    <div class="abs tab" style="left:0;width:175px">Most Recent</div>
    <div class="abs tab active" style="left:175px;width:212px;text-align:center">Most Popular</div>
    <div class="abs tab" style="left:387px;width:243px">Deal of the day</div>
    <div class="abs divider"></div>

    <div class="abs thumb" role="img" aria-label="Laptop listed for swap" style="left:35px;top:100px;width:108px;height:78px;background:linear-gradient(135deg,#7fb8b0,#c9ccce 60%,#9a9ea2)"></div>
    <p class="abs blurb" style="left:14px;top:190px;width:232px;text-align:center">this is just as example. this is just as example. this is just as example. this is just as example. this is just as example. this is just</p>
    <svg class="abs play" style="left:211px;top:345px" viewBox="0 0 30 30"><circle cx="15" cy="15" r="15" fill="#000"/><path d="M11 8l10 7-10 7z" fill="#fff"/></svg>

    <div class="abs thumb" role="img" aria-label="Smartphone listed for swap" style="left:317px;top:142px;width:72px;height:132px;background:linear-gradient(#333,#1a1a1a);border-radius:8px"></div>
    <p class="abs blurb" style="left:410px;top:127px;width:170px">&nbsp;&nbsp;this is just as example. this is just as example. this is just as example. this is just as example. this is just as example. this is just</p>
    <svg class="abs play" style="left:563px;top:345px" viewBox="0 0 30 30"><circle cx="15" cy="15" r="15" fill="#000"/><path d="M11 8l10 7-10 7z" fill="#fff"/></svg>
  </section>

  <section class="abs join">
    <div class="abs join-tab active">Join Now</div>
    <div class="abs join-tab other">Sign in</div>
    <div class="abs join-bar"></div>
    <div class="abs join-field" style="top:107px">Username</div>
    <div class="abs join-field" style="top:155px">Email</div>
    <div class="abs join-field" style="top:205px">Password</div>
    <div class="abs join-field" style="top:253px">Confirm password</div>
    <div class="abs signup">Sign up</div>
    <a class="abs forgot">Forgot your email?</a>
    <div class="abs join-foot"></div>
  </section>

</div>
</body>
</html>
```